mapleridgegroup Business Card Design

Business card with logo design for mapleridgegroup. We are a group of professional project managers based on the Pareto Principle that 80% of the work is done by 20% of the people. I have a makeshift logo that uses a pi chart with 30% and 20% and the 20% pie slice is set slightly out and up. Have played around with a teal and orange colour scheme.

Industry/Entity Type

Business

Contact Information for Business Card

Gareth Pembroke
Director
mapleridgegroup

0452 803716

```html
<!DOCTYPE html>
<html lang="en">
<head>
<meta charset="utf-8">
<title>mapleridgegroup Business Card</title>
<link rel="stylesheet" href="https://fonts.googleapis.com/css2?family=Open+Sans:wght@400;600;700&display=swap">
<style>
  :root {
    --page: #e9e7e4;
    --card: #ffffff;
    --ink: #3a3a3a;
    --ink-soft: #555555;
    --teal: #2a8f9c;
    --orange: #f26a3c;
    --icon: #3d3d3d;
    --rule: #9a9a9a;
  }
  html, body {
    margin: 0;
    width: 1200px;
    height: 899px;
    overflow: hidden;
    background: var(--page);
    font-family: "Open Sans", Arial, sans-serif;
  }
  .business-card {
    position: absolute;
    left: 180px;
    top: 210px;
    width: 840px;
    height: 480px;
    background: var(--card);
    border-radius: 42px;
    overflow: hidden;
    box-shadow: 0 10px 30px rgba(0,0,0,0.12);
  }
  .footer-band {
    position: absolute;
    left: 0;
    right: 0;
    bottom: 0;
    height: 84px;
    background: var(--orange);
    border-top: 6px solid var(--teal);
  }
  .brand {
    position: absolute;
    left: 120px;
    top: 92px;
    display: flex;
    align-items: center;
    gap: 18px;
  }
  .brand-dot {
    width: 64px;
    height: 64px;
    border-radius: 50%;
    background: var(--orange);
  }
  .brand-name {
    font-size: 46px;
    font-weight: 400;
    color: var(--teal);
    letter-spacing: -0.5px;
  }
  .holder {
    position: absolute;
    right: 465px;
    top: 196px;
    text-align: right;
    color: var(--ink);
  }
  .holder-name {
    font-size: 21px;
    font-weight: 700;
    margin: 0;
    line-height: 1.2;
  }
  .holder-title {
    font-size: 15px;
    color: var(--ink-soft);
    margin: 2px 0 0;
  }
  .holder-address {
    font-size: 15px;
    color: var(--ink-soft);
    margin: 26px 0 0;
    line-height: 1.55;
  }
  .divider {
    position: absolute;
    left: 395px;
    top: 198px;
    width: 1px;
    height: 132px;
    background: var(--rule);
  }
  .contact-list {
    position: absolute;
    left: 412px;
    top: 196px;
    margin: 0;
    padding: 0;
    list-style: none;
    font-size: 15px;
    color: var(--ink-soft);
  }
  .contact-list li {
    display: flex;
    align-items: center;
    gap: 10px;
    height: 26px;
  }
  .contact-icon {
    width: 16px;
    height: 16px;
    flex: none;
  }
</style>
</head>
<body>
  <div class="business-card">
    <div class="brand">
      <span class="brand-dot"></span>
      <span class="brand-name">mapleridgegroup</span>
    </div>

    <div class="holder">
      <p class="holder-name">Gareth Pembroke</p>
      <p class="holder-title">Owner / C.E.O</p>
      <p class="holder-address">Suite # 114, Cove Bldg, NY<br>40218</p>
    </div>

    <div class="divider"></div>

    <ul class="contact-list">
      <li>
        <svg class="contact-icon" viewBox="0 0 16 16" aria-hidden="true"><circle cx="8" cy="8" r="8" fill="var(--icon)"/><path d="M5 4.5 l1.5 0 l0.8 2 l-1 0.8 a5 5 0 0 0 2.4 2.4 l0.8 -1 l2 0.8 l0 1.5 a1 1 0 0 1 -1 1 A7 7 0 0 1 4 5.5 a1 1 0 0 1 1 -1z" fill="#fff"/></svg>
        0452 803716
      </li>
      <li>
        <svg class="contact-icon" viewBox="0 0 16 16" aria-hidden="true"><circle cx="8" cy="8" r="8" fill="var(--icon)"/><rect x="5.5" y="3.5" width="5" height="9" rx="1" fill="#fff"/></svg>
        0452 610294
      </li>
      <li>
        <svg class="contact-icon" viewBox="0 0 16 16" aria-hidden="true"><circle cx="8" cy="8" r="8" fill="var(--icon)"/><rect x="4" y="6" width="8" height="5" rx="1" fill="#fff"/><rect x="5.5" y="3.8" width="5" height="2.4" fill="#fff"/></svg>
        0452 337180
      </li>
      <li>
        <svg class="contact-icon" viewBox="0 0 16 16" aria-hidden="true"><circle cx="8" cy="8" r="8" fill="var(--icon)"/><rect x="4" y="5" width="8" height="6" fill="#fff"/><path d="M4 5 L8 8.5 L12 5" stroke="var(--icon)" stroke-width="1" fill="none"/></svg>
        hello@mapleridgegroup.com
      </li>
      <li>
        <svg class="contact-icon" viewBox="0 0 16 16" aria-hidden="true"><circle cx="8" cy="8" r="8" fill="var(--icon)"/><circle cx="8" cy="8" r="4" stroke="#fff" stroke-width="1.2" fill="none"/><path d="M4 8 H12 M8 4 V12" stroke="#fff" stroke-width="1"/></svg>
        www.mapleridgegroup.com
      </li>
    </ul>

    <div class="footer-band"></div>
  </div>
</body>
</html>
```